Law firm website marketed direct to many individual clients

I need someone to design a very basic website for a law firm that will be very eye catching. It's going to be a single-paged, scrolling website with a small number of folds. I have uploaded a simple word document that outlines the basics of what I thought could be the layout, but I am open to suggestion on font, size, shades of color, organization, etc. etc. Essentially the website just needs to be a very efficient and visually appealing way of conveying some simple messages.

Target Market(s)

High volumes of individuals who have gotten into a car accident and then google on their phones a lawyer to hire to represent them.

Industry/Entity Type

Legal

Number of Pages Required

1 page

Font styles to use
Serif
Sans Serif

Colors
34a7d7
85cae6
0592cd

Requirements
Must have
• Must be bright and grab the users attention with color scheme and layout. The different sections should be done in such a way that they can fit entirely onto one smart phone or tablet screen.
Nice to have
• I'd like to try and see what it looks like if in the middle somewhere there is a fold that says "MEET YOUR ATTORNEYS" and includes individual photos of two attorneys, one on the left side and one on the right. And then a small bio section on them. I don't want the photos to include a square or rectangle background, I want the person in the photo to be superimposed on top of whatever pattern or background you have in the fold.
Should not have
• Do not want too much text. Anything more than 2 sentences in any single place is unacceptable.

```html
<!DOCTYPE html>
<html lang="en">
<head>
<meta charset="utf-8">
<title>Harborline Law Group</title>
<link href="https://fonts.googleapis.com/css2?family=Arimo:ital,wght@0,400;1,400&family=Lato:wght@400;700;900&family=Raleway:wght@400;500;700&display=swap" rel="stylesheet">
<style>
:root{
  --blue:#34a7d7;
  --blue-deep:#0592cd;
  --blue-soft:#85cae6;
  --white:#ffffff;
  --ink:#333333;
  --grey:#777777;
  --paper:#efefef;
  --footer:#383838;
}
*{margin:0;padding:0;box-sizing:border-box}
html,body{width:726px;height:1200px;overflow:hidden;background:var(--white)}
body{position:relative;font-family:"Arimo",Arial,sans-serif;color:var(--ink)}
.abs{position:absolute}
.icon-ring{position:absolute;border-radius:50%;display:flex;align-items:center;justify-content:center}

/* hero */
.hero{position:absolute;left:0;top:0;width:726px;height:410px;overflow:hidden}
.hero-photo{position:absolute;inset:0;background:linear-gradient(160deg,#4a4642 0%,#2c2a28 40%,#3b3531 70%,#1f1d1c 100%)}
.hero-shade{position:absolute;inset:0;background:rgba(0,0,0,.25)}
.brand{left:48px;top:16px;font-family:"Raleway",sans-serif;font-size:26px;font-weight:400;color:var(--blue)}
.top-call{left:456px;top:24px;font-size:14px;color:var(--white)}
.top-ring{left:519px;top:13px;width:38px;height:38px;border:2px solid var(--blue)}
.top-number{left:567px;top:20px;font-size:19px;color:var(--white);font-weight:400}
.headline{left:0;width:726px;top:184px;text-align:center;font-family:"Lato",sans-serif;font-weight:900;font-size:51px;color:var(--white);letter-spacing:.5px}
.headline .accent{color:var(--blue)}
.hero-call{left:0;width:726px;top:254px;text-align:center;font-size:25px;color:#e8e8e8}
.hero-ring{left:344px;top:298px;width:38px;height:38px;border:2px solid var(--blue)}

/* features */
.feature-band{position:absolute;left:0;top:410px;width:726px;height:75px;background:var(--blue);border-top:5px solid #2f9ccb}
.feature{position:absolute;top:446px;width:150px;text-align:center}
.feature-ring{position:relative;margin:0 auto;width:77px;height:77px;border:4px solid var(--blue-deep);background:var(--white);border-radius:50%;display:flex;align-items:center;justify-content:center}
.feature-title{margin-top:12px;font-family:"Raleway",sans-serif;font-size:11.5px;font-weight:500;color:var(--blue);line-height:14px}
.feature-text{margin-top:8px;font-size:8.6px;color:var(--grey);line-height:13px}

/* money band */
.money{position:absolute;left:0;top:628px;width:726px;height:252px;background:var(--blue);text-align:center;color:var(--white)}
.money-kicker{position:absolute;left:0;width:726px;top:38px;font-family:"Raleway",sans-serif;font-size:22px;font-weight:400}
.money-title{position:absolute;left:0;width:726px;top:67px;font-family:"Raleway",sans-serif;font-size:28px;font-weight:700}
.money-ring{left:341px;top:111px;width:44px;height:44px;background:var(--white)}
.money-call{position:absolute;left:0;width:726px;top:166px;font-size:25px;font-style:italic}
.money-link{position:absolute;left:0;width:726px;top:200px;font-family:"Raleway",sans-serif;font-size:12px;font-style:italic;text-decoration:underline;color:var(--white)}

/* info */
.info{position:absolute;left:0;top:880px;width:726px;height:244px;background:var(--paper)}
.info h2{position:absolute;left:48px;font-family:"Raleway",sans-serif;font-weight:700;font-size:19.5px;color:var(--blue)}
.info p{position:absolute;left:48px;font-size:8.8px;line-height:15px;color:#555}
.info-call{position:absolute;left:48px;top:188px;font-size:18px;font-style:italic;color:#222}
.attorney-photo{position:absolute;left:538px;top:28px;width:144px;height:216px;border-radius:60px 60px 10px 10px;background:linear-gradient(180deg,#c9d4e2 0%,#a9bcd3 60%,#8fa6c2 100%)}

/* footer */
.footer{position:absolute;left:0;top:1124px;width:726px;height:76px;background:var(--footer);color:var(--white)}
.foot-ring{top:24px;width:30px;height:30px;border:1.5px solid var(--blue)}
.foot-address{left:88px;top:28px;font-size:8.6px;line-height:14px;color:#eee}
.foot-number{left:305px;top:31px;font-size:12px;color:#eee}
.foot-copy{right:50px;top:33px;font-size:9px;color:#ddd}
.foot-copy .name{color:var(--blue)}
</style>
</head>
<body>

<header class="hero">
  <div class="hero-photo" role="img" aria-label="Photo of a lawyer relaxing in a leather chair with feet on a desk in a city office"></div>
  <div class="hero-shade"></div>
  <div class="abs brand">Harborline Law Group</div>
  <div class="abs top-call">Call Us :</div>
  <div class="icon-ring top-ring">
    <svg width="18" height="18" viewBox="0 0 24 24"><path fill="#34a7d7" d="M6.6 10.8a15.1 15.1 0 0 0 6.6 6.6l2.2-2.2c.3-.3.7-.4 1-.2 1.1.4 2.3.6 3.6.6.6 0 1 .4 1 1V20c0 .6-.4 1-1 1A17 17 0 0 1 3 4c0-.6.4-1 1-1h3.5c.6 0 1 .4 1 1 0 1.3.2 2.5.6 3.6.1.3 0 .7-.2 1z"/></svg>
  </div>
  <div class="abs top-number">555-014-2290</div>
  <h1 class="abs headline"><span class="accent">ACCIDENT?</span> INJURED?</h1>
  <div class="abs hero-call">Call Us : 555-014-2290</div>
  <div class="icon-ring hero-ring">
    <svg width="18" height="18" viewBox="0 0 24 24"><path fill="#34a7d7" d="M6.6 10.8a15.1 15.1 0 0 0 6.6 6.6l2.2-2.2c.3-.3.7-.4 1-.2 1.1.4 2.3.6 3.6.6.6 0 1 .4 1 1V20c0 .6-.4 1-1 1A17 17 0 0 1 3 4c0-.6.4-1 1-1h3.5c.6 0 1 .4 1 1 0 1.3.2 2.5.6 3.6.1.3 0 .7-.2 1z"/></svg>
  </div>
</header>

<section class="features">
  <div class="feature-band"></div>

  <div class="feature" style="left:47px">
    <div class="feature-ring">
      <svg width="40" height="40" viewBox="0 0 40 40"><path d="M6 17 20 6l14 11" fill="none" stroke="#0592cd" stroke-width="2.5"/><circle cx="20" cy="20" r="7" fill="#0592cd"/><text x="20" y="24.5" text-anchor="middle" font-size="11" font-family="Arial" font-weight="700" fill="#fff">$</text><rect x="10" y="29" width="20" height="2.5" fill="#0592cd"/><rect x="8" y="33" width="24" height="2.5" fill="#0592cd"/></svg>
    </div>
    <div class="feature-title">LOW FEES</div>
    <div class="feature-text">We charge less, so you keep more.</div>
  </div>

  <div class="feature" style="left:207px">
    <div class="feature-ring">
      <svg width="40" height="40" viewBox="0 0 40 40"><rect x="12" y="7" width="22" height="15" rx="2" fill="none" stroke="#0592cd" stroke-width="2.2"/><path d="M6 13h19v15H14l-5 5v-5H6z" fill="#fff" stroke="#0592cd" stroke-width="2.2"/><circle cx="11" cy="20.5" r="1.6" fill="#0592cd"/><circle cx="15.5" cy="20.5" r="1.6" fill="#0592cd"/><circle cx="20" cy="20.5" r="1.6" fill="#0592cd"/></svg>
    </div>
    <div class="feature-title">FREE CONSULTATION</div>
    <div class="feature-text">It's always free to talk to us.</div>
  </div>

  <div class="feature" style="left:367px">
    <div class="feature-ring">
      <svg width="40" height="40" viewBox="0 0 40 40"><path fill="#0592cd" d="M12 17.5a18 18 0 0 0 8 8l2.7-2.7c.4-.4.9-.5 1.3-.3 1.3.4 2.8.7 4.3.7.7 0 1.2.5 1.2 1.2v4.3c0 .7-.5 1.2-1.2 1.2A21 21 0 0 1 7.4 9.2C7.4 8.5 8 8 8.6 8h4.3c.7 0 1.2.5 1.2 1.2 0 1.5.3 3 .7 4.3.1.4 0 .9-.3 1.3z"/><path d="M22 7a11 11 0 0 1 10 10M22 12a6 6 0 0 1 5 5" fill="none" stroke="#0592cd" stroke-width="2.2" stroke-linecap="round"/></svg>
    </div>
    <div class="feature-title">GET STARTED USING ONLY<br>YOUR PHONE</div>
    <div class="feature-text">No need to come to the office, sign up using your phone.</div>
  </div>

  <div class="feature" style="left:528px">
    <div class="feature-ring">
      <svg width="44" height="40" viewBox="0 0 44 40"><circle cx="11" cy="11" r="4.5" fill="#0592cd"/><circle cx="33" cy="11" r="4.5" fill="#0592cd"/><path d="M4 32V22c0-3 2-5 5-5h4c2 0 3 1 4 2l5 4 5-4c1-1 2-2 4-2h4c3 0 5 2 5 5v10z" fill="#0592cd"/></svg>
    </div>
    <div class="feature-title">SPEAK DIRECTLY<br>TO A LAWYER</div>
    <div class="feature-text">No staff screening. Talk right to a lawyer on your first call.</div>
  </div>
</section>

<section class="money">
  <div class="money-kicker">YOUR CASE</div>
  <div class="money-title">YOUR MONEY</div>
  <div class="icon-ring money-ring">
    <svg width="22" height="22" viewBox="0 0 24 24"><path fill="#34a7d7" d="M6.6 10.8a15.1 15.1 0 0 0 6.6 6.6l2.2-2.2c.3-.3.7-.4 1-.2 1.1.4 2.3.6 3.6.6.6 0 1 .4 1 1V20c0 .6-.4 1-1 1A17 17 0 0 1 3 4c0-.6.4-1 1-1h3.5c.6 0 1 .4 1 1 0 1.3.2 2.5.6 3.6.1.3 0 .7-.2 1z"/></svg>
  </div>
  <div class="money-call">Call Us : 555-014-2290</div>
  <a class="money-link">LEARN MORE</a>
</section>

<section class="info">
  <h2 style="top:36px">NO FEE UNLESS WE WIN</h2>
  <p style="top:66px;width:400px">We don't get paid unless you get paid. It's as simple as that. We let our results do the talking for us.</p>
  <h2 style="top:116px">QUESTIONS ABOUT ANYTHING?</h2>
  <p style="top:146px;width:490px">We're here to help. Feel free to call us at 555-014-2290 to speak to one of our attorneys. With extensive experience in helping clients get the results that they want, our team is always just a phone call away</p>
  <div class="info-call">Call Us : 555-014-2290</div>
  <div class="attorney-photo" role="img" aria-label="Smiling attorney in shirt and tie with arms crossed"></div>
</section>

<footer class="footer">
  <div class="icon-ring foot-ring" style="left:48px">
    <svg width="14" height="16" viewBox="0 0 24 28"><path d="M12 2a8 8 0 0 0-8 8c0 6 8 15 8 15s8-9 8-15a8 8 0 0 0-8-8z" fill="none" stroke="#34a7d7" stroke-width="2.5"/><circle cx="12" cy="10" r="3" fill="#34a7d7"/></svg>
  </div>
  <div class="abs foot-address">Harborline Law Group Main Office<br>100 Example Street, Riverton, LA 00000</div>
  <div class="icon-ring foot-ring" style="left:263px">
    <svg width="14" height="14" viewBox="0 0 24 24"><path fill="#34a7d7" d="M6.6 10.8a15.1 15.1 0 0 0 6.6 6.6l2.2-2.2c.3-.3.7-.4 1-.2 1.1.4 2.3.6 3.6.6.6 0 1 .4 1 1V20c0 .6-.4 1-1 1A17 17 0 0 1 3 4c0-.6.4-1 1-1h3.5c.6 0 1 .4 1 1 0 1.3.2 2.5.6 3.6.1.3 0 .7-.2 1z"/></svg>
  </div>
  <div class="abs foot-number">555-014-2290</div>
  <div class="abs foot-copy">© 2016 <span class="name">Harborline Law Group</span> All rights reserved.</div>
</footer>

</body>
</html>
```